Book cover The seven quiet ledgers

I need a book cover for a 6 x 9 inches book.

I prefer white background with clean lines. Bleed is 0.125 inches and spine is 0.27024

The back of the cover must consider the space for the ISBN barcode: 2" wide and 1.2" tall. The bottom of this ISBN barcode is located 1/4" up from the bottom trim line of the cover. The right side of the ISBN barcode is located 1/4" to the left of the spine.

Front cover should have title and subtitle plus author's name. The book is in Spanish so:

title: Las siete brújulas olvidadas
subtitle: Abra las puertas de su calma interior
author: Marta Quintero Blaine

the information about the book is here www.thesevenquietledgers.example

the back cover should have three blocks of information, a summary of the book, testimonials and about the author with a picture (leave space for a picture) Also, there should be a note with our website and bulk purchases

This is the information on the back. No need to add what is in parenthesis.

(about author) Marta Quintero Blaine es una de las expertas internacionales en creación de riqueza. Ha formado ocho empresas y una fundación, incluyendo el primer fondo de inversiones de capital semilla en Chile. Reconocida autora y expositora, ha recorrido el mundo varias veces presentando su sistema Fortivan®

Top (summary)
La mayoría de las personas no estan satisfechas con su prosperidad. Prueban estoy y aquello, hacen cursos, leen libros y mientras todos dicen lo que hay que hacer, nadie explica lo que NO hay que hacer. Si ud. Está estancado, este libro es para ud.

Testimonios (Testimonial):
Un libro que llega al alma. Tomás Brevo.
No solo es importante saber que hacer, sino estar alerta a lo que no debemos hacer. Dennis Marlow.
El sistema para cambiar hábitos es excelente. Rodrigo Ulloa-paz
Nos permite remendar esos pequeños detalles que afectan nuestra autoestima. Margaret Hollis
Una manera sana de acumular y manejar la prosperidad que nos merecemos. Bevan Moody
Nos recuerda como nuestra percepción subconsciente del dinero afecta nuestro éxito financiero Lorena Vance.

Ventas al mayor rkelmor@fortivan.example
www.thesevenquietledgers.example

Target Market(s)

Individuals who feel they are working hard but are not getting the results they want regarding their financial well being.

this is NOT a book to get out of debt or to get rich quick.

this is a book for people who are serious about their lives and feel that, although they are working hard, they are stuck.

the summary of the book in English is found here: www.thesevenquietledgers.example
I am also changing working on the third edition of the book in English, so I wouldn't be using the same cover. you can see the book for sale on bookvale. "The Seven Quiet Ledgers"

Requirements
Must have
• Clean lines, white background, elegant, professional but human.
Nice to have
• an image that represents breaking a habit or getting unstuck. I thought about an anchor or a weigh or car brakes.
Should not have
• Bright colors, faces, pictures

```html
<!DOCTYPE html>
<html lang="es">
<head>
<meta charset="utf-8">
<title>Las siete brújulas olvidadas — cubierta</title>
<link rel="stylesheet" href="https://fonts.googleapis.com/css2?family=Oswald:wght@500&family=Roboto+Condensed:wght@400;700&display=swap">
<style>
  :root {
    --stage: #000000;
    --paper: #ffffff;
    --ink: #000000;
    --mist: #9a9a9a;
    --gold: #b8955e;
    --spine: #999999;
    --photo: #b3b3b3;
    --body: #222222;
    --display: "Oswald", "Arial Narrow", sans-serif;
    --text: "Roboto Condensed", "Arial Narrow", sans-serif;
  }
  * { box-sizing: border-box; margin: 0; padding: 0; }
  html, body { width: 1200px; height: 900px; overflow: hidden; background: var(--stage); }
  .canvas { position: relative; width: 1200px; height: 900px; }

  .panel {
    position: absolute;
    top: 106px;
    height: 658px;
    background: var(--paper);
    overflow: hidden;
  }
  .panel--back { left: 88px; width: 442px; }
  .panel--front { left: 669px; width: 443px; }

  .display {
    position: absolute;
    font-family: var(--display);
    font-weight: 500;
    text-transform: uppercase;
    white-space: nowrap;
    line-height: 1;
    letter-spacing: -0.02em;
  }
  .title { font-size: 72px; color: var(--ink); top: 66px; }
  .subtitle { font-size: 50px; color: var(--mist); top: 125px; }
  .author { font-size: 126px; color: var(--gold); top: 155px; }

  .panel--front .display { left: 31px; }
  .panel--back .title { right: 122px; }
  .panel--back .subtitle { right: 237px; }
  .panel--back .author { right: 20px; }

  .barcode-space {
    position: absolute;
    left: 285px;
    top: 561px;
    width: 153px;
    height: 92px;
    background: var(--ink);
  }

  .spine {
    position: absolute;
    left: 590px;
    top: 92px;
    width: 21px;
    height: 686px;
    background: var(--spine);
  }
  .spine__label {
    position: absolute;
    left: 50%;
    top: 204px;
    transform: translateX(-50%) rotate(90deg);
    transform-origin: center;
    writing-mode: vertical-rl;
    transform: translateX(-50%);
    font-family: var(--display);
    font-weight: 500;
    font-size: 13px;
    text-transform: uppercase;
    white-space: nowrap;
    letter-spacing: -0.01em;
    color: var(--ink);
  }
  .spine__label .spine__author { color: var(--paper); }

  .copy {
    position: absolute;
    font-family: var(--text);
    font-size: 9.6px;
    line-height: 12.4px;
    color: var(--body);
    text-align: justify;
  }
  .author-photo {
    position: absolute;
    left: 31px;
    top: 305px;
    width: 76px;
    height: 74px;
    background: var(--photo);
  }
  .bio { left: 118px; top: 305px; width: 207px; }
  .summary { left: 31px; top: 396px; width: 294px; }
  .testimonials { left: 31px; top: 451px; width: 294px; }
  .copy strong { color: var(--ink); font-weight: 700; }
  .copy .quote-by { color: var(--gold); font-weight: 700; }
</style>
</head>
<body>
<main class="canvas">

  <section class="panel panel--back" aria-label="Contraportada">
    <p class="display title">Las siete brújulas olvidadas</p>
    <p class="display subtitle">Abra las puertas de su calma interior</p>
    <p class="display author">Marta Quintero Blaine</p>
    <div class="barcode-space" aria-label="Espacio reservado para el ISBN"></div>
  </section>

  <section class="spine" aria-label="Lomo">
    <p class="spine__label">Las siete brújulas olvidadas <span class="spine__author">Marta Quintero Blaine</span></p>
  </section>

  <section class="panel panel--front" aria-label="Portada">
    <h1 class="display title">Las siete brújulas olvidadas</h1>
    <p class="display subtitle">Abra las puertas de su calma interior</p>
    <p class="display author">Marta Quintero Blaine</p>

    <div class="author-photo" role="img" aria-label="Espacio para la foto de la autora"></div>
    <p class="copy bio">Marta Quintero Blaine es una de las expertas internacionales en creación de riqueza. Ha formado ocho empresas y una fundación, incluyendo el primer fondo de inversiones de capital semilla en Chile. Reconocida autora y expositora, ha recorrido el mundo varias veces presentando su sistema Fortivan®</p>

    <p class="copy summary"><strong>Top</strong> La mayoría de las personas no estan satisfechas con su prosperidad. Prueban estoy y aquello, hacen cursos, leen libros y mientras todos dicen lo que hay que hacer, nadie explica lo que NO hay que hacer. Si ud. Está estancado, este libro es para ud.</p>

    <p class="copy testimonials"><strong>Testimonios</strong> Un libro que llega al alma - <span class="quote-by">Tomás Brevo</span> No solo es importante saber que hacer, sino estar alerta a lo que no debemos hacer - <span class="quote-by">Dennis Marlow</span> El sistema para cambiar hábitos es excelente - <span class="quote-by">Rodrigo Ulloa-paz</span> Nos permite remendar esos pequeños detalles que afectan nuestra autoestima - <span class="quote-by">Margaret Hollis</span> Una manera sana de acumular y manejar la prosperidad que nos merecemos - <span class="quote-by">Bevan Moody</span> Nos recuerda como nuestra percepción subconsciente del dinero afecta nuestro éxito financiero - <span class="quote-by">Lorena Vance</span></p>
  </section>

</main>
</body>
</html>
```